Church Lanterns Over Millbrook Gospel Booklet Design

We need a booklet designed that we will be printing to hand out in our community. Wording for each page will be provided and we need graphic design to produce the layouts in a format ready for print. Booklet will be 4.75" x 4.75" square and a total of 12 pages: 1 cover page front, 1 cover page back, 10 inside pages some of which will be full spread across 2 pages.

Target Market(s)

English speaking Westerners

Industry/Entity Type

Religious

Font styles to use
Serif

Colors
ffffff
85abd2
0292cd
33b8a4
5c5c5c

Requirements
Must have
• Minimalist design with clean look described in attached document
Nice to have
• Aesthetically pleasing graphics, crisp fonts, excellent turn around times
Should not have
• Effeminate design, busy look with too much graphic and text

```html
<!DOCTYPE html>
<html lang="en">
<head>
<meta charset="utf-8">
<title>Lanterns Over Millbrook – Gospel Booklet</title>
<link href="https://fonts.googleapis.com/css2?family=Cinzel:wght@500;600&family=Roboto:wght@400;500;700&family=Roboto+Condensed:wght@400;500&display=swap" rel="stylesheet">
<style>
  :root{
    --backdrop:#f4e8b9;
    --paper:#ffffff;
    --ink:#2b2b2b;
    --ink-soft:#5c5c5c;
    --gold:#d9b40c;
    --frame:rgba(255,255,255,.9);
    --sky-blue:#85abd2;
    --warm:#f2a25a;
    --sunset:#e9785a;
  }
  *{box-sizing:border-box;margin:0;padding:0}
  html,body{width:960px;height:1200px;overflow:hidden}
  body{background:var(--backdrop);position:relative;font-family:"Roboto",sans-serif;color:var(--ink)}
  .sheet{position:absolute;background:var(--paper);box-shadow:3px 5px 8px rgba(0,0,0,.28);overflow:hidden}
  .spread{position:absolute;display:flex;box-shadow:0 6px 6px -3px rgba(0,0,0,.25);overflow:hidden}
  .page{position:relative;flex:1;height:100%;background:var(--paper);overflow:hidden}
  .photo{position:absolute}
  .frame{position:absolute;inset:8px;border:1px solid var(--frame);pointer-events:none}
  .frame-left{right:0;border-right:none}
  .frame-right{left:0;border-left:none}

  /* covers */
  .cover-title{position:absolute;left:0;right:0;top:104px;text-align:center;font-family:"Cinzel",serif;font-weight:600;color:var(--ink);line-height:1}
  .cover-title .line-one{display:block;font-size:25px;letter-spacing:.5px}
  .cover-title .line-two{display:block;font-size:22px;margin-top:6px}
  .web-band{position:absolute;left:0;right:0;top:242px;height:13px;background:var(--gold);color:#fff;font-size:7.5px;letter-spacing:2.4px;text-align:center;line-height:13px;font-weight:500}
  .address-box{position:absolute;left:24px;top:26px;width:230px;height:88px;border:1px solid #cfcfcf;background:#fff}

  /* text */
  .copy{position:absolute;font-size:5.6px;line-height:1.32;color:var(--ink-soft)}
  .copy p+p{margin-top:3px}
  .justify{text-align:justify}
  .heading{font-size:6.6px;font-weight:700;color:var(--ink);text-transform:uppercase;line-height:1.3}
  .verse{font-weight:700;color:var(--ink);font-size:6.4px;line-height:1.3}
  .ref{text-align:right;color:var(--ink);font-size:6.6px;font-weight:500}
  .bullets{list-style:none}
  .bullets li{position:relative;padding-left:5px;margin-top:3px}
  .bullets li::before{content:"•";position:absolute;left:0}

  .closing{position:absolute;left:0;right:0;top:36px;text-align:center;font-family:"Roboto Condensed",sans-serif;color:#231a0c;text-transform:uppercase}
  .closing .small{font-size:8px;line-height:1.7}
  .closing .large{font-size:12.5px;line-height:1.3}
</style>
</head>
<body>

<!-- Front cover -->
<section class="sheet" style="left:198px;top:56px;width:276px;height:274px">
  <h1 class="cover-title"><span class="line-one">LANTERNS</span><span class="line-two">OVER MILLBROOK</span></h1>
  <div class="web-band">www.millbrooklanterns.org</div>
</section>

<!-- Back cover -->
<section class="sheet" style="left:491px;top:56px;width:277px;height:274px">
  <div class="photo" role="img" aria-label="Faded sunrise with raised hands" style="inset:0;background:linear-gradient(180deg,#fff 30%,#f3efe6 55%,#ebe6dc 80%,#f1eee8 100%)"></div>
  <div class="address-box"></div>
  <div class="web-band" style="top:244px">www.millbrooklanterns.org</div>
</section>

<!-- Spread 1 -->
<section class="spread" style="left:45px;top:390px;width:426px;height:210px">
  <div class="page">
    <div class="photo" role="img" aria-label="Crowd facing a cross at sunrise" style="inset:0;background:linear-gradient(180deg,#b9a3c8 0%,#f4d2c4 30%,#f6e6dc 45%,#9a8a8e 70%,#5f5a66 100%)"></div>
    <div class="frame frame-left"></div>
  </div>
  <div class="page">
    <div class="photo" role="img" aria-label="Open hands reaching toward sunlight over green trees" style="left:0;right:0;top:70px;bottom:0;background:linear-gradient(180deg,#fff 0%,#e7c774 25%,#a8a64a 50%,#6a8a3a 80%,#5b7e33 100%)"></div>
    <div class="frame frame-right"></div>
    <div class="copy" style="left:10px;right:10px;top:29px;text-align:center;font-size:6.2px">
      <p>God willingly created the universe, meaning he envisioned, designed, and made us.</p>
      <p class="verse" style="margin-top:4px">“In the beginning God created the heavens and the earth.”<br><span style="font-weight:500">(Genesis 1:1)</span></p>
    </div>
  </div>
</section>

<!-- Spread 2 -->
<section class="spread" style="left:483px;top:390px;width:424px;height:210px">
  <div class="page">
    <div class="photo" role="img" aria-label="Silhouetted hands holding a glowing cross at sunset" style="left:0;right:0;top:100px;bottom:0;background:linear-gradient(180deg,#fff 0%,#f3c9a0 25%,#e99a5a 55%,#3a2a22 85%,#2a1f1a 100%)"></div>
    <div class="frame frame-left"></div>
    <div class="copy" style="left:15px;right:14px;top:16px">
      <p class="heading">This reality establishes some foundational truths for all of us:</p>
      <ul class="bullets">
        <li>God loves us - he didn't have to create us; we are here because he couldn't imagine life without us.</li>
        <li>God is the proper authority in our lives - if he designed and made us, he rightfully owns us.</li>
        <li>God knows the purpose of our lives - if he designed and made us, he knows why we are here.</li>
        <li>God's truth is the truth we need - if he designed and made us, he knows what it takes for life to go well for us.</li>
      </ul>
    </div>
  </div>
  <div class="page">
    <div class="photo" role="img" aria-label="Cross on a hilltop against a sunset sky" style="left:0;right:0;top:66px;bottom:0;background:linear-gradient(180deg,#fff 0%,#f0b9a2 20%,#e58766 45%,#d9a04e 65%,#7c4c3a 85%,#3b2a25 100%)"></div>
    <div class="frame frame-right"></div>
    <div class="copy justify" style="left:12px;right:12px;top:22px">
      <p>But we, mankind, have all rejected God's authority in our lives. And because he rightfully owns us, our rebellion against God is a grave injustice; an act of treason for which we deserve to be cut off from God forever.</p>
      <p class="verse" style="margin-top:4px">•&nbsp; “For the wages of sin is death...”</p>
      <p class="ref">- (Romans 6:23)</p>
    </div>
  </div>
</section>

<!-- Spread 3 -->
<section class="spread" style="left:45px;top:648px;width:426px;height:212px">
  <div class="page">
    <div class="photo" role="img" aria-label="Worship crowd under a warm sunset sky" style="left:0;top:0;bottom:0;width:103px;background:linear-gradient(180deg,#fbe3d2 0%,#f39b6a 25%,#e06a4a 45%,#8a6470 70%,#3f3542 100%)"></div>
    <div class="photo" role="img" aria-label="Faded crowd in grey tones" style="left:103px;right:0;top:100px;bottom:0;background:linear-gradient(180deg,#fff 0%,#d9d9d9 50%,#a8a8a8 100%)"></div>
    <div class="copy justify" style="left:113px;right:14px;top:20px">
      <p>This alienation from God is evident in a myriad of ways including poverty, crime, conflict in our relationships, and our internal struggles. But worse, when we die, we must face the consequences for our rejection of God by spending eternity in hell - a lake of fire created by God as the place where our treason is brought to justice.</p>
    </div>
  </div>
  <div class="page">
    <div class="photo" role="img" aria-label="Faded raised hands in grey tones" style="left:0;top:120px;bottom:0;width:118px;background:linear-gradient(180deg,#fff 0%,#cfcfcf 55%,#8c8c8c 100%)"></div>
    <div class="photo" role="img" aria-label="Glowing cross above worshippers with raised hands" style="right:0;top:0;bottom:0;width:95px;background:linear-gradient(180deg,#fbe0d2 0%,#f6cdb6 30%,#fbe9df 45%,#e7a6a0 70%,#5a4a78 100%)"></div>
    <div class="copy justify" style="left:17px;width:90px;top:18px">
      <p>But God does not want you to pay for your own sins. God loves us so much he sent his only son to save us. Jesus Christ died on the cross to serve our sentence for our rebellion against God and rose again on the third day. Since Christ paid our full penalty, we can be completely forgiven and reconciled to God.</p>
      <p class="verse" style="margin-top:4px">•&nbsp;“For God so loved the world that he sent his one and only son that whosoever believes in him will not perish but have eternal life.”</p>
      <p class="ref">- (John 3:16)</p>
    </div>
  </div>
</section>

<!-- Spread 4 -->
<section class="spread" style="left:484px;top:648px;width:426px;height:213px">
  <div class="page">
    <div class="photo" role="img" aria-label="Parent and child walking toward a cross at sunrise" style="inset:0;background:linear-gradient(180deg,#9cc1d8 0%,#e8d6c4 35%,#f6ece0 55%,#d9a98a 75%,#5f4a44 100%)"></div>
    <div class="frame frame-left"></div>
  </div>
  <div class="page">
    <div class="photo" role="img" aria-label="Silhouetted hands holding a glowing cross at sunset" style="left:0;right:0;top:110px;bottom:0;background:linear-gradient(180deg,#fff 0%,#f1d0b4 25%,#e89f62 55%,#3a2a22 85%,#2a1f1a 100%)"></div>
    <div class="frame frame-right"></div>
    <div class="copy justify" style="left:14px;right:14px;top:18px">
      <p class="heading" style="font-size:6.3px">Here is what you must do to be saved:</p>
      <p>First, ask Jesus Christ to save you (Since he is God, he can hear you): Acknowledge that God is the rightful authority of the universe and your life. Apologize to him for your rebellion against God. Ask Jesus Christ to come into your life as your Lord and Savior. This decision will immediately trigger his miracle of salvation in you. God now lives in you!</p>
      <p class="verse" style="margin-top:4px">•&nbsp;“If you confess with your mouth that Jesus is Lord and believe in your heart that God raised him from the dead, you will be saved.”</p>
      <p class="ref">- (Romans 10:9)</p>
    </div>
  </div>
</section>

<!-- Spread 5 -->
<section class="spread" style="left:260px;top:909px;width:427px;height:213px">
  <div class="page">
    <div class="photo" role="img" aria-label="Worshippers with raised hands under rays of light" style="left:0;right:0;top:70px;bottom:0;background:linear-gradient(180deg,#fff 0%,#c9dcee 30%,#85abd2 60%,#3f5f9a 100%)"></div>
    <div class="copy justify" style="left:15px;right:14px;top:20px">
      <p>Next, God has given us the Bible and his church as the key tools for us to grow in our understanding of God and our personal relationship with him. So, it is essential you find a local church that believes the Bible is 100% true. Tell one of the pastors you are a brand new Christian and they will help you from there.</p>
    </div>
  </div>
  <div class="page">
    <div class="photo" role="img" aria-label="Golden sky over a mountain peak" style="inset:0;background:linear-gradient(180deg,#e9a646 0%,#f2c36c 30%,#d9a25a 55%,#8a5a3a 75%,#3a261c 100%)"></div>
    <div class="frame frame-right" style="right:8px;border-right:1px solid var(--frame)"></div>
    <div class="closing">
      <p class="small">If you confess with your mouth,</p>
      <p class="large">“Jesus is Lord,”</p>
      <p class="small">and believe in your heart that</p>
      <p class="small">God raised him from the dead,</p>
      <p class="large">You will be saved.</p>
    </div>
  </div>
</section>

</body>
</html>
```